Design a building access mobile app for Wopel by Quillstone Access Controls

Hello, We're looking for an awesome designer to create an app design for our app Wopel, by Quillstone Access Controls. the mobile app allows employees open their office doors with their mobile phone. this means they don't have to use those plastic card badges or keys. We like clean modern design, dark and light themes. We don't have a logo yet.

Target Market(s)

Commercial and employees

Industry/Entity Type

Building

Font styles to use
Sans Serif
Other font styles liked:
• Oswald extra light

Requirements
Must have
• nice clean design

```html
<!DOCTYPE html>
<html lang="en">
<head>
<meta charset="utf-8">
<title>Wopel — Settings</title>
<link rel="stylesheet" href="https://fonts.googleapis.com/css2?family=Oswald:wght@200;300&family=Roboto:wght@400&display=swap">
<style>
  :root {
    --bg-top: #232323;
    --bg-bottom: #171717;
    --text: #f2f2f2;
    --toggle-on: #5ec6df;
    --toggle-off: #8a8a8a;
    --knob: #ffffff;
    --teal-top: #22b8cf;
    --teal-bottom: #3a8fbf;
    --sheet: #ffffff;
    --chevron: #4a90d9;
  }
  * { margin: 0; padding: 0; box-sizing: border-box; }
  html, body { width: 675px; height: 1200px; overflow: hidden; }
  body {
    position: relative;
    background: linear-gradient(170deg, var(--bg-top), var(--bg-bottom));
    color: var(--text);
    font-family: "Oswald", sans-serif;
    font-weight: 200;
  }
  .status-bar {
    position: absolute; top: 6px; left: 12px; right: 8px; height: 26px;
    display: flex; align-items: center; justify-content: space-between;
    font-family: "Roboto", sans-serif; font-size: 21px; color: var(--text);
  }
  .status-left, .status-right { display: flex; align-items: center; gap: 6px; }
  .status-time { position: absolute; left: 0; right: 0; text-align: center; pointer-events: none; color: #ffffff; }

  .settings-menu { position: absolute; left: 30px; top: 0; width: 482px; }
  .menu-title, .menu-item {
    position: absolute; left: 0; width: 482px; height: 44px;
    display: flex; align-items: center; justify-content: space-between;
    font-size: 33px; font-weight: 200; letter-spacing: -0.4px; transform: translateY(-50%);
  }
  .toggle {
    width: 48px; height: 30px; border-radius: 15px; position: relative;
    background: var(--toggle-off);
  }
  .toggle::after {
    content: ""; position: absolute; top: 1px; left: 1px;
    width: 28px; height: 28px; border-radius: 50%; background: var(--knob);
    box-shadow: 0 1px 3px rgba(0,0,0,.35);
  }
  .toggle.is-on { background: var(--toggle-on); }
  .toggle.is-on::after { left: 19px; }

  .app-preview {
    position: absolute; left: 548px; top: 183px; width: 127px; height: 833px;
    overflow: hidden; background: var(--sheet);
  }
  .preview-header {
    position: absolute; inset: 0 0 auto 0; height: 393px;
    background: linear-gradient(170deg, var(--teal-top), var(--teal-bottom));
  }
  .preview-status {
    position: absolute; top: 6px; left: 8px; white-space: nowrap;
    font-family: "Roboto", sans-serif; font-size: 13px; color: #fff;
    display: flex; align-items: center; gap: 4px;
  }
  .preview-menu-icon { position: absolute; left: 17px; top: 44px; }
  .preview-number {
    position: absolute; left: 61px; top: 221px; font-size: 36px; font-weight: 300;
    color: #fff; white-space: nowrap; line-height: 1;
  }
  .preview-sub {
    position: absolute; left: 120px; top: 272px; font-size: 34px; font-weight: 300;
    color: #fff; line-height: 1;
  }
  .preview-back { position: absolute; left: 44px; top: 597px; }
</style>
</head>
<body>
  <header class="status-bar">
    <div class="status-left">
      <span>●●●○○</span><span>Veltro</span>
      <svg width="20" height="16" viewBox="0 0 20 16"><path d="M10 15l3-3.5a4.5 4.5 0 0 0-6 0z M3.5 8a9 9 0 0 1 13 0l-1.8 2a6.5 6.5 0 0 0-9.4 0z M0 4.3a14 14 0 0 1 20 0l-1.8 2a11.5 11.5 0 0 0-16.4 0z" fill="#fff"/></svg>
    </div>
    <div class="status-time">1:23 AM</div>
    <div class="status-right">
      <svg width="12" height="20" viewBox="0 0 12 20"><path d="M1 5l9 9-4.5 4.5V1.5L10 6 1 15" fill="none" stroke="#aaa" stroke-width="1.5"/></svg>
      <span>77%</span>
      <svg width="42" height="20" viewBox="0 0 42 20"><rect x="1" y="2" width="36" height="16" rx="3" fill="none" stroke="#fff" stroke-width="1.5"/><rect x="3.5" y="4.5" width="26" height="11" rx="1" fill="#fff"/><rect x="38.5" y="7" width="2.5" height="6" rx="1" fill="#fff"/></svg>
    </div>
  </header>

  <nav class="settings-menu" aria-label="Settings">
    <h1 class="menu-title" style="top:291px">SETTINGS</h1>
    <div class="menu-item" style="top:392px"><span>AUTO LOGOUT</span><span class="toggle is-on"></span></div>
    <div class="menu-item" style="top:493px"><span>AUTO OPEN</span><span class="toggle is-on"></span></div>
    <div class="menu-item" style="top:593px"><span>AUTO CLOSE</span><span class="toggle"></span></div>
    <div class="menu-item" style="top:694px"><span>AUTO FAR</span><span class="toggle"></span></div>
    <div class="menu-item" style="top:794px"><span>FINGERPRINT</span></div>
    <div class="menu-item" style="top:894px"><span>HELP</span></div>
  </nav>

  <aside class="app-preview" aria-label="Main screen">
    <div class="preview-header">
      <div class="preview-status">
        <span>●●●○○</span><span>Veltro</span>
        <svg width="14" height="11" viewBox="0 0 20 16"><path d="M10 15l3-3.5a4.5 4.5 0 0 0-6 0z M3.5 8a9 9 0 0 1 13 0l-1.8 2a6.5 6.5 0 0 0-9.4 0z M0 4.3a14 14 0 0 1 20 0l-1.8 2a11.5 11.5 0 0 0-16.4 0z" fill="#fff"/></svg>
      </div>
      <svg class="preview-menu-icon" width="26" height="20" viewBox="0 0 26 20"><path d="M0 2h26M0 10h26M0 18h26" stroke="#fff" stroke-width="2.2"/></svg>
      <div class="preview-number">1410</div>
      <div class="preview-sub">S</div>
    </div>
    <svg class="preview-back" width="22" height="36" viewBox="0 0 22 36"><path d="M20 1L3 18l17 17" fill="none" stroke="var(--chevron)" stroke-width="2.2"/></svg>
  </aside>
</body>
</html>
```